IT Company needs Website for new Web and Mobile products for Sports and Fitness

Background:

We developed web based white label frontend web solution, backend services and white label mobile apps for to log, analyze, share and control sport and fitness activities. The name of this product suite is "Trelvano" (http://trelvano-example.com)

This products will be used by customers that provide platforms and community systems for sport and fitness. One of the major USP's is, that our technology i open for nearly all common formats, devices and apps out in the market. This means, you can just upload your data directly from device, file or app - e.G. Brindle, Vextor, Kalppi, StrideNook, Jogmelda, BipBop and much others.

Two current concrete examples/References

(1) MyOrvane
It's an international platform from orvane for runners. It provides individual training lans and a training log. MyOrvane uses the Backend Product "Trelvano Hub" (see http://hub.trelvano-example.net for a landing page) to integrate device, file and app support. Before this, every user has to track his training with manual inputs

(2) Paceharbor and qel-zine
Both are German customers. Paceharor is focused on runners. qel-zine is focused on Triatheletes. Both use the Product "Trelvano Web". This is a complete web solution with web based frontend solutions for athletes and coaches.

What do we need?
We need website layout for B2B for our products. We don't need lot's of pages. We need the pretty and nice layout, so we can derive the pages we need.

IMPORTANT
We don't talk about the webpages for the product itself (this will be a different project in future). We talk about a website, explaining the products)
Updates

Hi all,

we just start reviewing the first designs, and try to give feedback as detailed as possible. We attached a PDF document, to describe the the products a little bit more detailed. 

As written in the description, in the end we have two different sections. One is the usual stuff like "start page", "about", "contact", "disclaimer", "pricing", "blah...." and one will be the Developer Section, the "Tec Section". This ist aimed to developers (of our customers) that will integrate our products in there existing system or which will integrate our services in there own software.  This "pages" are more like "documentation", so easy to read and cool to look at (cause developers likes it cool, but straight)

Dear all,

we just do the final review. Cause this week is with heavy load, it takes some time...

Cheers

Ulrik

Target Market(s)

* Platforms and Communities for sport, health and fitness
* Gyms

Industry/Entity Type

Concrete

Font styles to use
Sans Serif

Requirements
Must have
• * Templates shall base on bootstrap. If not, it shall be easily realized on our site with bootstrap or out of the box "full responsive"

* HTML5 / CSS3
Nice to have
• PAGES
- Start Page
- Generic Template (from which we can derive additional pages)
- Contact Page
- Disclaimer Page
- Blog/News Page
- "About us" Page (can be combined with disclaimer)
- One Example product page (in end we have 3 products), shall show (if you need product details, let me know)
- product and it's description
- pricing information
- Add-Ons for the product
- Developer Section Page (Start Point for developers, where the finde "basic technical concepts and developer API's
- Example Developer Page for technical concept
- Example Developer Page for API

LOGO ISSUE
You can use an align to the Logo attached OR provide a new logo. The given logo is a logo for our own B2C Website http://trelvano-example.net. It's not really necessary, that the logo or the color must be used for the product website. Maybe it will be better if it's a complete new one, to avoid irritation between Trelvano as a B2B product and trelvano-example.net as a B2C platform.
Should not have
• No Flash and other proprietary technologies

```html
<!DOCTYPE html>
<html lang="en">
<head>
<meta charset="utf-8">
<title>Trelvano – Digital Sports Services</title>
<link href="https://fonts.googleapis.com/css2?family=Source+Sans+3:ital,wght@0,400;0,600;0,700;1,400&display=swap" rel="stylesheet">
<style>
:root{
  --orange:#f07d0a;
  --orange-dark:#d9650a;
  --ink:#333;
  --text:#666;
  --muted:#888;
  --rule:#e2e2e2;
  --footer:#343434;
  --white:#fff;
}
*{margin:0;padding:0;box-sizing:border-box}
html,body{width:904px;height:1200px;overflow:hidden;background:var(--white)}
body{position:relative;font-family:"Source Sans 3",Arial,sans-serif;color:var(--text)}
.abs{position:absolute}
.site-header{position:absolute;left:0;top:0;width:904px;height:100px;border-top:2px solid var(--orange);background:linear-gradient(#fff,#f3f3f3)}
.brand{left:98px;top:34px;font-size:32px;font-weight:700;color:var(--ink);letter-spacing:.5px;display:flex;align-items:center;gap:8px}
.brand-mark{width:20px;height:20px;background:var(--orange);border-radius:50%}
.btn{background:linear-gradient(#f79a2a,var(--orange-dark));color:#fff;font-weight:600;text-transform:uppercase;display:flex;align-items:center;justify-content:center;border-radius:2px}
.login{left:650px;top:15px;width:63px;height:23px;font-size:10px}
.util{left:727px;top:22px;font-size:10px;color:var(--ink)}
.main-nav{left:382px;top:70px;display:flex;font-size:10px;text-transform:uppercase;color:var(--ink)}
.main-nav span{white-space:nowrap}
.main-nav .sep{margin:0 13px}
.main-nav .active{color:var(--orange)}
.search{left:778px;top:63px;width:27px;height:24px;border-radius:2px}
.hero{left:0;top:100px;width:904px;height:378px;background:linear-gradient(180deg,#4d6c8e 0%,#8092a2 40%,#d7a25a 72%,#f0a032 86%,#1a1009 97%)}
.hero-card{left:530px;top:218px;width:300px;height:164px;background:rgba(255,255,255,.86);text-align:right;padding:16px 19px}
.hero-card h1{font-weight:400;font-size:27px;color:var(--ink);line-height:1.1}
.hero-card p{font-size:11px;line-height:18px;color:var(--ink);margin-top:11px}
.cta{right:19px;top:119px;width:116px;height:27px;font-size:10px}
.dots{left:750px;top:455px;display:flex;gap:3px}
.dots i{width:11px;height:11px;border-radius:50%;background:#bbb}
.dots i:first-child{background:#fff}
.welcome h2{font-size:20px;font-weight:400;color:var(--ink)}
.accent{color:var(--orange)}
.copy{font-size:10px;line-height:15px;color:var(--text)}
.more{font-size:9px;color:var(--orange);text-transform:uppercase}
.rule{height:2px;background:var(--rule)}
.section-title{font-size:20px;font-weight:400;color:var(--ink)}
.video{left:98px;top:810px;width:226px;height:129px;background:linear-gradient(135deg,#6f7a70,#3d3f40 60%,#5b5f60)}
.play{left:185px;top:849px}
.feature-list{list-style:none;font-size:10.5px;color:var(--ink)}
.feature-list li{height:19.5px}
.feature-list li::before{content:"»";color:var(--orange);margin-right:6px}
.vrule{left:563px;top:766px;width:1px;height:220px;background:var(--rule)}
.arrow{width:19px;height:18px;background:#333;color:#fff;font-size:10px;display:flex;align-items:center;justify-content:center;border-radius:2px}
.portrait{left:581px;top:809px;width:61px;height:61px;background:linear-gradient(#8b6b55,#5a4a40)}
.partners{left:98px;top:1028px;width:708px;display:flex;justify-content:space-around;font-size:11px;font-weight:700;color:#8a8a8a}
.site-footer{left:0;top:1110px;width:904px;height:90px;background:var(--footer);color:#eee}
.footer-links{left:98px;top:24px;font-size:10px}
.copyright{left:98px;top:48px;font-size:9.5px;color:#ccc}
.social{left:716px;top:29px;display:flex;gap:3px}
.social i{width:20px;height:20px;background:#777;border-radius:2px}
</style>
</head>
<body>
<header class="site-header">
  <div class="abs brand"><span class="brand-mark"></span>Trelvano</div>
  <div class="abs btn login">Login</div>
  <div class="abs util">Manual&nbsp; | &nbsp;My sport</div>
  <nav class="abs main-nav">
    <span class="active">About Trelvano</span><span class="sep">|</span>
    <span>Service</span><span class="sep">|</span>
    <span>Blog</span><span class="sep">|</span>
    <span>Support</span><span class="sep">|</span>
    <span>News</span><span class="sep">|</span>
    <span>Contact</span>
  </nav>
  <div class="abs btn search">
    <svg width="14" height="14" viewBox="0 0 14 14"><circle cx="8.5" cy="5.5" r="4" fill="none" stroke="#fff" stroke-width="2"/><line x1="5.5" y1="8.5" x2="1.5" y2="12.5" stroke="#fff" stroke-width="2.5" stroke-linecap="round"/></svg>
  </div>
</header>

<section class="abs hero" role="img" aria-label="Sunset sky with a running athlete silhouette and a smartphone showing the app"></section>
<div class="abs hero-card">
  <h1>Digital Sports Services</h1>
  <p>Our mission is the path from the port to the computer<br>to automate consistently and steadily eliminate.</p>
  <div class="abs btn cta">Get started now</div>
</div>
<div class="abs dots"><i></i><i></i><i></i><i></i></div>

<section class="welcome">
  <h2 class="abs" style="left:98px;top:509px">Welcome to <span class="accent">Trelvano</span></h2>
  <p class="abs copy" style="left:98px;top:550px;width:708px">Lorem ipsum dolor sit amet, consectetur adipisicing elit, sed do eiusmod tempor incididunt ut labore et dolore magna aliqua. Ut enim ad minim veniam, quis nostrud exercitation ullamco laboris nisi ut aliquip ex ea commodo consequat. Duis aute irure dolor in reprehenderit in voluptate velit esse cillum dolore eu fugiat nulla pariatur. Excepteur sint occaecat cupidatat non proident, sunt in culpa qui officia deserunt mollit anim id est laborum.</p>
  <p class="abs copy" style="left:98px;top:612px;width:708px">Sed ut perspiciatis unde omnis iste natus error sit voluptatem accusantium doloremque laudantium, totam rem aperiam, eaque ipsa quae ab illo inventore veritatis et quasi architecto beatae vitae dicta sunt explicabo. Nemo enim ipsam voluptatem quia voluptas sit aspernatur aut odit aut fugit, sed quia consequuntur magni dolores eos qui ratione voluptatem sequi nesciunt. Neque porro quisquam est, qui dolorem ipsum quia dolor sit amet, consectetur, adipisci velit, sed quia non numquam eius modi tempora incidunt ut labore et dolore magnam aliquam quaerat voluptatem. Ut enim ad minima veniam, quis nostrum exercitationem ullam corporis suscipit laboriosam, nisi ut aliquid ex ea commodi consequatur.</p>
  <div class="abs more" style="left:98px;top:706px">Read more &gt;&gt;</div>
</section>

<div class="abs rule" style="left:98px;top:746px;width:708px"></div>

<section class="how">
  <h2 class="abs section-title" style="left:98px;top:770px">How it Works</h2>
  <div class="abs video" role="img" aria-label="Road cyclist riding through a corner"></div>
  <svg class="abs play" width="54" height="54" viewBox="0 0 54 54"><circle cx="27" cy="27" r="25" fill="rgba(0,0,0,.25)" stroke="#fff" stroke-width="3"/><path d="M20 15 L39 27 L20 39 Z" fill="#fff"/></svg>
  <p class="abs copy" style="left:341px;top:806px;width:210px;font-size:10.5px">Et harum quidem rerum facilis est et expedita distinctio. Nam libero tempore, cum soluta nis est eligendi optio cumque.</p>
  <ul class="abs feature-list" style="left:341px;top:866px">
    <li>unterstützt mehr als 100 Sportarten</li>
    <li>versteht Geräte, Apps und Formate</li>
    <li>motiviert mit einzigartigen Events</li>
    <li>bringt Sportler vor Ort zusammen</li>
    <li>verlangt kein spezielles Equipment</li>
  </ul>
</section>

<div class="abs vrule"></div>

<section class="testimonials">
  <h2 class="abs section-title accent" style="left:581px;top:770px">Testimonials</h2>
  <div class="abs arrow" style="left:764px;top:774px">‹</div>
  <div class="abs arrow" style="left:785px;top:774px;color:var(--orange)">›</div>
  <div class="abs portrait" role="img" aria-label="Portrait photo of the customer"></div>
  <p class="abs copy" style="left:653px;top:807px;width:154px;color:var(--ink)">Temporibus autem quibusdam et aut officiis debitis aut rerum necessitatibus saepe eveniet ut et voluptate repudiandae sint</p>
  <p class="abs copy" style="left:581px;top:880px;width:225px">Et molestiae non recusandae. Itaque earum rerum hic tenetur a sapiente delectus, ut aut reiciendis.</p>
  <div class="abs accent" style="left:600px;top:924px;width:202px;text-align:right;font-size:11px">by Dario Velmont</div>
  <div class="abs" style="left:600px;top:944px;width:202px;text-align:right;font-size:10px;font-style:italic;color:var(--muted)">from Newyork</div>
</section>

<div class="abs rule" style="left:98px;top:1006px;width:708px"></div>
<div class="abs partners">
  <span>Brindle</span><span>Vextor</span><span>Cyclomar</span><span>Heuvel</span><span>Tamiro</span><span>Wendlow</span><span>Wuvo</span><span>Sorrim</span><span>TrackTally</span><span>Nixo+</span><span>Taxo</span><span>Konzepta</span>
</div>
<div class="abs rule" style="left:98px;top:1068px;width:708px"></div>

<footer class="abs site-footer">
  <div class="abs footer-links">About Trelvano | Press | Blog | Support | Imprint | Terms | Privacy |</div>
  <div class="abs copyright">© 2013 Trelvano All Right Reserved.</div>
  <div class="abs social" aria-label="Social links: Chirp, Facenet, Vidtube, RSS"><i></i><i></i><i></i><i style="background:var(--orange)"></i></div>
</footer>
</body>
</html>
```